依頼概要
初めまして。よろしくお願いいたします。

依頼内容
※エコー(赤ちゃん)ポスターのデザイン依頼

※エコー写真をスキャンして嵌め込みますので、そちらを想定したテンプレート型のポスターデザインをお願いいたします。

※エコーの枚数は3・6・9枚の何れかでお願いいたします。

※子供の名前 身長体重 出産時間 等

ポスターデザインのイメージや雰囲気は
デザイナー様各々におまかせしております。

```html
<!DOCTYPE html>
<html lang="en">
<head>
<meta charset="utf-8">
<title>Thank you for being born! — Echo Poster</title>
<link rel="stylesheet" href="https://fonts.googleapis.com/css2?family=Great+Vibes&family=Bodoni+Moda:wght@400;500&family=Libre+Baskerville&display=swap">
<style>
  :root {
    --paper: #ffffff;
    --ink: #2b2a33;
    --gold: #d9a93f;
    --gold-deep: #c28f2a;
    --echo-dark: #0d0d0d;
    --echo-light: #5a5a5a;
  }
  html, body { margin: 0; padding: 0; overflow: hidden; background: var(--paper); }
  .poster {
    position: relative;
    width: 851px;
    height: 1200px;
    background: var(--paper);
    overflow: hidden;
    color: var(--ink);
    font-family: "Libre Baskerville", serif;
  }
  .decor { position: absolute; inset: 0; width: 851px; height: 1200px; }
  .clinic {
    position: absolute;
    right: 26px;
    top: 22px;
    text-align: right;
    font-size: 12px;
    line-height: 1.6;
  }
  .title {
    position: absolute;
    left: 0;
    width: 851px;
    text-align: center;
    font-family: "Great Vibes", cursive;
    font-size: 96px;
    line-height: 1;
    margin: 0;
    font-weight: 400;
  }
  .title-top { top: 72px; }
  .title-bottom { top: 238px; }
  .heart-for {
    position: absolute;
    left: 376px;
    top: 168px;
    width: 82px;
    height: 72px;
  }
  .heart-word {
    position: absolute;
    left: 376px;
    top: 178px;
    width: 82px;
    text-align: center;
    font-family: "Great Vibes", cursive;
    color: var(--paper);
    font-size: 30px;
  }
  .echo-grid {
    position: absolute;
    left: 53px;
    top: 397px;
    display: grid;
    grid-template-columns: repeat(3, 220px);
    grid-auto-rows: 158px;
    column-gap: 42px;
    row-gap: 28px;
  }
  .echo-slot {
    background: radial-gradient(ellipse at 45% 55%, var(--echo-light) 0%, #262626 45%, var(--echo-dark) 75%);
    border: 2px solid #1a1a1a;
    box-sizing: border-box;
  }
  .baby-name {
    position: absolute;
    top: 960px;
    left: 0;
    width: 851px;
    text-align: center;
    font-family: "Bodoni Moda", serif;
    font-weight: 500;
    font-size: 68px;
    letter-spacing: 2px;
    margin: 0;
  }
  .birth-details {
    position: absolute;
    top: 1068px;
    left: 0;
    width: 851px;
    margin: 0;
  }
  .detail {
    position: absolute;
    width: 200px;
    margin-left: -100px;
    text-align: center;
  }
  .detail dt { font-size: 13px; margin-bottom: 10px; }
  .detail dd { margin: 0; font-size: 17px; font-family: "Bodoni Moda", serif; font-weight: 500; letter-spacing: 1px; }
</style>
</head>
<body>
<main class="poster">
  <svg class="decor" viewBox="0 0 851 1200" aria-hidden="true">
    <g fill="var(--gold)">
      <circle cx="612" cy="58" r="34"/>
      <circle cx="824" cy="298" r="12"/>
      <circle cx="14" cy="520" r="18"/>
      <circle cx="765" cy="985" r="40"/>
      <circle cx="46" cy="1008" r="9"/>
      <circle cx="822" cy="1120" r="10"/>
      <circle cx="92" cy="78" r="6"/>
    </g>
    <g fill="var(--ink)">
      <circle cx="82" cy="62" r="6"/>
      <circle cx="800" cy="258" r="4"/>
      <circle cx="770" cy="45" r="3"/>
      <circle cx="590" cy="110" r="4"/>
      <circle cx="60" cy="985" r="7"/>
      <circle cx="36" cy="1160" r="5"/>
      <circle cx="810" cy="1170" r="5"/>
      <circle cx="790" cy="1080" r="3"/>
    </g>
    <g fill="none" stroke="var(--ink)" stroke-width="1.5">
      <circle cx="40" cy="80" r="5"/>
      <circle cx="768" cy="320" r="6"/>
      <circle cx="240" cy="1075" r="5"/>
      <circle cx="20" cy="1050" r="4"/>
    </g>
    <g stroke="var(--ink)" stroke-width="2" stroke-linecap="round">
      <line x1="130" y1="185" x2="188" y2="250"/>
      <line x1="120" y1="215" x2="178" y2="272"/>
      <line x1="132" y1="262" x2="172" y2="290"/>
      <line x1="720" y1="185" x2="662" y2="250"/>
      <line x1="730" y1="215" x2="672" y2="272"/>
      <line x1="718" y1="262" x2="678" y2="290"/>
    </g>
  </svg>

  <div class="clinic">
    <div>name</div>
    <div>Ob-Gynecological Clinic</div>
  </div>

  <h1 class="title title-top">Thank you</h1>
  <svg class="heart-for" viewBox="0 0 82 72" aria-hidden="true">
    <path d="M41 70 C18 52 2 38 2 20 C2 9 11 2 21 2 C30 2 37 8 41 15 C45 8 52 2 61 2 C71 2 80 9 80 20 C80 38 64 52 41 70 Z" fill="var(--ink)"/>
  </svg>
  <span class="heart-word">for</span>
  <p class="title title-bottom">being born!</p>

  <section class="echo-grid">
    <div class="echo-slot" role="img" aria-label="Ultrasound scan 1"></div>
    <div class="echo-slot" role="img" aria-label="Ultrasound scan 2"></div>
    <div class="echo-slot" role="img" aria-label="Ultrasound scan 3"></div>
    <div class="echo-slot" role="img" aria-label="Ultrasound scan 4"></div>
    <div class="echo-slot" role="img" aria-label="Ultrasound scan 5"></div>
    <div class="echo-slot" role="img" aria-label="Ultrasound scan 6"></div>
    <div class="echo-slot" role="img" aria-label="Ultrasound scan 7"></div>
    <div class="echo-slot" role="img" aria-label="Ultrasound scan 8"></div>
    <div class="echo-slot" role="img" aria-label="Ultrasound scan 9"></div>
  </section>

  <h2 class="baby-name">NAME</h2>

  <dl class="birth-details">
    <div class="detail" style="left:142px"><dt>birthday</dt><dd>0000.00.00</dd></div>
    <div class="detail" style="left:352px"><dt>time</dt><dd>00:00</dd></div>
    <div class="detail" style="left:525px"><dt>weight</dt><dd>0000g</dd></div>
    <div class="detail" style="left:712px"><dt>height</dt><dd>0000cm</dd></div>
  </dl>
</main>
</body>
</html>
```